Mineral Drinking Water Label Design

We need a label design for a new bottled drinking water based in (either Azurine or Dar Es Salaam, decision is not yet finalized), Tanzania on the coast of East Africa.

We will use underground aquifers as our only source of raw water(pre treated water).

Which will then be treated through osmosis process, then the mineral water will be bottled in standard 500ml, 1000ml and 1500 ml plastic PET bottles for customer consumption.

We have a vision of expanding our supply network to cover the entire country. Therefore, we expect the label to communicate trust, purity, cleanliness, healthiness of water contained.

The uniqueness and attractiveness of the label/logo is of utmost importance.

With regards to water brand name, we prefer that you use your own imagination and creativity to come up with a name that might be more suited to your individual design.

Note: Different shades of blue are mainly associated with drinking water in Tanzania, however feel free to use any other colors.

Target Market(s)

Upper Class citizens, Hotels, Large Supermarkets etc

Font styles to use
Script

Colors

Designer to choose colors to be used in the design.

```html
<!DOCTYPE html>
<html lang="en">
<head>
<meta charset="utf-8">
<title>Azurine Mineral Water Label</title>
<link href="https://fonts.googleapis.com/css2?family=Oswald:wght@500&family=Open+Sans:wght@400;600;700&display=swap" rel="stylesheet">
<style>
  :root {
    --navy: #1b2a6b;
    --deep: #0b2a86;
    --mid: #1f6fcf;
    --sky: #3ea3e8;
    --guide: #2f8fd8;
    --white: #ffffff;
    --mist: #c9ccd6;
  }
  * { margin: 0; padding: 0; box-sizing: border-box; }
  html, body { width: 1200px; height: 1000px; overflow: hidden; background: var(--white); }
  .canvas { position: relative; width: 1200px; height: 1000px; font-family: "Open Sans", Arial, sans-serif; color: var(--navy); }
  .art { position: absolute; inset: 0; }
  .size-title { position: absolute; top: 84px; left: 0; width: 1200px; text-align: center; font-family: "Open Sans", Arial, sans-serif; font-weight: 700; font-size: 26px; color: var(--navy); }
  .bleed-note { position: absolute; top: 128px; left: 290px; font-size: 10px; font-weight: 700; color: var(--guide); background: var(--white); padding: 0 3px; }
  .cut-note { position: absolute; top: 138px; left: 956px; font-size: 10px; font-weight: 700; color: var(--navy); }
  .story { position: absolute; top: 185px; left: 120px; width: 183px; font-size: 9.6px; line-height: 11px; text-align: justify; color: var(--navy); }
  .story p { margin-bottom: 3px; }
  .brand { position: absolute; top: 186px; left: 430px; width: 310px; text-align: center; font-family: "Oswald", Arial, sans-serif; font-weight: 500; font-size: 72px; line-height: 90px; color: var(--deep); }
  .product { position: absolute; left: 497px; width: 200px; text-align: center; font-family: "Oswald", Arial, sans-serif; font-weight: 500; color: var(--white); }
  .product-name { top: 343px; font-size: 19px; }
  .product-volume { top: 384px; font-size: 18px; }
  .facts-head { position: absolute; top: 165px; left: 905px; width: 110px; text-align: center; font-size: 8.5px; line-height: 10px; color: var(--navy); }
  .facts-head .small { font-size: 7px; }
  .facts { position: absolute; top: 190px; left: 920px; width: 87px; height: 139px; border: 1.5px solid var(--navy); padding: 2px 3px; font-size: 5.3px; line-height: 6.6px; color: var(--navy); }
  .facts h3 { font-size: 10px; line-height: 11px; font-weight: 600; border-bottom: 2.5px solid var(--navy); padding-bottom: 1px; }
  .facts .row { display: flex; justify-content: space-between; border-bottom: 0.7px solid var(--navy); padding: 1.5px 0; }
  .facts .thick { border-bottom-width: 2px; }
  .facts .note { margin-top: 3px; font-size: 4.2px; line-height: 5px; }
  .distributor { position: absolute; top: 341px; left: 908px; font-size: 9.5px; line-height: 10.5px; color: var(--white); }
  .recycle { position: absolute; top: 390px; left: 922px; display: flex; align-items: center; gap: 3px; font-size: 6.5px; font-weight: 700; color: var(--white); }
</style>
</head>
<body>
<div class="canvas">
  <svg class="art" width="1200" height="1000" viewBox="0 0 1200 1000">
    <defs>
      <linearGradient id="sea" x1="0" y1="0" x2="0" y2="1" gradientUnits="userSpaceOnUse" gradientTransform="" >
      </linearGradient>
      <linearGradient id="seaFill" x1="0" y1="225" x2="0" y2="436" gradientUnits="userSpaceOnUse">
        <stop offset="0" stop-color="#b9d8f2"/>
        <stop offset="0.35" stop-color="#3ea3e8"/>
        <stop offset="0.65" stop-color="#1f6fcf"/>
        <stop offset="1" stop-color="#0a2276"/>
      </linearGradient>
      <linearGradient id="mistFill" x1="0" y1="0" x2="1" y2="0">
        <stop offset="0" stop-color="#9aa0b3" stop-opacity="0.7"/>
        <stop offset="0.35" stop-color="#ffffff" stop-opacity="0"/>
        <stop offset="0.7" stop-color="#ffffff" stop-opacity="0"/>
        <stop offset="1" stop-color="#9aa0b3" stop-opacity="0.7"/>
      </linearGradient>
      <linearGradient id="bottleFill" x1="0" y1="0" x2="1" y2="0">
        <stop offset="0" stop-color="#9fc3e6"/>
        <stop offset="0.5" stop-color="#e4f0fb"/>
        <stop offset="1" stop-color="#8fb7e0"/>
      </linearGradient>
    </defs>

    <rect class="bleed-line" x="57" y="135" width="1065" height="301" fill="none" stroke="var(--guide)" stroke-width="1.2" stroke-dasharray="4 3"/>
    <path class="wave-shadow" d="M57,215 C250,290 420,318 560,316 C720,314 900,255 1122,212 L1122,260 L57,260 Z" fill="url(#mistFill)"/>
    <path class="wave-sea" d="M57,226 C250,300 420,325 560,322 C720,318 900,262 1122,225 L1122,436 L57,436 Z" fill="url(#seaFill)"/>
    <rect class="die-cut" x="71" y="155" width="1031" height="263" rx="14" fill="none" stroke="var(--navy)" stroke-width="1"/>
    <path d="M1077,145 L1085,151 M1085,151 L1080,151 M1085,151 L1085,146" stroke="var(--navy)" stroke-width="1" fill="none"/>

    <g role="img" aria-label="Product bottle photograph showing the label wrapped on a clear 500ml water bottle">
      <rect x="538" y="493" width="117" height="467" rx="34" fill="url(#bottleFill)"/>
    </g>
  </svg>

  <div class="size-title">7.75" x 2.0"</div>
  <div class="bleed-note">1/8th" Bleed</div>
  <div class="cut-note">Die cut line (Does not print)</div>

  <div class="story">
    <p>Lorem ipsum dolor sit amet, consectetur adipiscing elit, sed do eiusmod tempor incididunt ut labore et dolore magna aliqua. Ut enim ad minim veniam, quis nostrud exercitation ullamco laboris nisi ut aliquip ex ea commodo consequat.</p>
    <p>Duis aute irure dolor in reprehenderit in voluptate velit esse cillum dolore eu fugiat nulla pariatur.</p>
    <p>Excepteur sint occaecat cupidatat non proident, sunt in culpa qui officia deserunt mollit anim id est laborum.</p>
  </div>

  <div class="brand">Azurine</div>
  <div class="product product-name">MINERAL WATER</div>
  <div class="product product-volume">500ml</div>

  <div class="facts-head">Ultra Purified Water<br><span class="small">.5 Liter (16.9 FL.OZ.)</span></div>
  <div class="facts">
    <h3>Nutrition Facts</h3>
    <div>Serving Size 8.0 fl.oz. (240mL)</div>
    <div class="row thick">Servings per Container: 2</div>
    <div class="row thick">Calories 0</div>
    <div class="row"><span>Amount Per Serving</span><span>% Daily Value*</span></div>
    <div class="row"><span>Total Fat 0g</span><span>0%</span></div>
    <div class="row"><span>Sodium 0mg</span><span>0%</span></div>
    <div class="row"><span>Total Carbohydrate 0g</span><span>0%</span></div>
    <div class="row thick"><span>Protein 0g</span><span>0%</span></div>
    <div class="note">Not a significant source of other nutrients. *Percent Daily Values are based on a 2,000 calorie diet.</div>
  </div>

  <div class="distributor">Bottled and Distributed by:<br>Azurine Inc<br>Address<br>www.azurinewater.com</div>
  <div class="recycle">
    <svg width="18" height="18" viewBox="0 0 18 18" aria-hidden="true">
      <circle cx="9" cy="9" r="8.5" fill="var(--white)"/>
      <path d="M9,3.5 L12,8.5 L10.3,8.5 M12.5,13 L6.5,13 L7.5,11.5 M4.5,10 L7,5.5 L8,7" stroke="var(--deep)" stroke-width="1.4" fill="none"/>
    </svg>
    PLEASE RECYCLE
  </div>
</div>
</body>
</html>
```